Business Cards and others
Business cards, stationery, Powerpoint template and E-mail Header and Footer
Professional
Darian Lutrell
CEO
4827 Thornwick Ln
Fernhollow MD 21093
darian@velmorix.com
www.velmorix.com

```html
<!DOCTYPE html>
<html lang="en">
<head>
<meta charset="utf-8">
<title>Velmorix Business Card</title>
<link rel="stylesheet" href="https://fonts.googleapis.com/css2?family=Open+Sans:ital,wght@0,400;0,600;0,700;1,600&display=swap">
<style>
  :root {
    --backdrop: #e9e6e1;
    --card: #ffffff;
    --brand-blue: #2a9fd6;
    --deep-blue: #1577a8;
    --band-grey: #9c9ea1;
    --text-grey: #6d6f72;
    --text-dark: #4a4c4f;
  }
  * { margin: 0; padding: 0; box-sizing: border-box; }
  html, body {
    width: 1200px;
    height: 914px;
    overflow: hidden;
    background: var(--backdrop);
    font-family: "Open Sans", Arial, sans-serif;
  }
  .card {
    position: absolute;
    left: 40px;
    top: 37px;
    width: 1120px;
    height: 840px;
    background: var(--card);
    box-shadow: 0 6px 24px rgba(0,0,0,0.12);
    overflow: hidden;
  }
  .swoosh {
    position: absolute;
    inset: 0;
    width: 1120px;
    height: 840px;
  }
  .brand {
    position: absolute;
    left: 80px;
    top: 78px;
    display: flex;
    align-items: center;
    gap: 22px;
  }
  .brand-dot {
    width: 112px;
    height: 112px;
    border-radius: 50%;
    background: var(--brand-blue);
  }
  .brand-name {
    font-size: 84px;
    font-weight: 700;
    color: var(--brand-blue);
    letter-spacing: -1px;
  }
  .contact {
    position: absolute;
    left: 92px;
    top: 262px;
    list-style: none;
  }
  .contact li {
    display: flex;
    align-items: center;
    gap: 14px;
    font-size: 22px;
    line-height: 34px;
    color: var(--text-dark);
  }
  .contact .icon {
    width: 20px;
    height: 20px;
    flex: none;
  }
  .contact .spacer { width: 20px; flex: none; }
  .signature {
    position: absolute;
    right: 64px;
    bottom: 50px;
    text-align: right;
  }
  .person-name {
    font-size: 30px;
    font-weight: 600;
    font-style: italic;
    color: var(--brand-blue);
  }
  .person-role {
    font-size: 22px;
    color: var(--text-grey);
    margin-top: 4px;
  }
</style>
</head>
<body>
  <div class="card">
    <svg class="swoosh" viewBox="0 0 1120 840" aria-hidden="true">
      <path d="M600,0 Q1000,110 1120,620 L1120,0 Z" fill="var(--band-grey)"/>
      <path d="M680,0 Q1010,110 1120,565 L1120,0 Z" fill="var(--card)"/>
      <path d="M715,0 Q1030,100 1120,540 L1120,0 Z" fill="var(--brand-blue)"/>
      <path d="M860,0 Q1060,60 1120,250 L1120,0 Z" fill="var(--deep-blue)"/>
    </svg>

    <div class="brand">
      <div class="brand-dot"></div>
      <div class="brand-name">Velmorix</div>
    </div>

    <ul class="contact">
      <li>
        <svg class="icon" viewBox="0 0 20 20"><circle cx="10" cy="10" r="10" fill="var(--brand-blue)"/><path d="M10 4.5c-2.2 0-3.8 1.6-3.8 3.6 0 2.6 3.8 7 3.8 7s3.8-4.4 3.8-7c0-2-1.6-3.6-3.8-3.6zm0 5a1.4 1.4 0 1 1 0-2.8 1.4 1.4 0 0 1 0 2.8z" fill="#fff"/></svg>
        <span>4827 Thornwick Ln</span>
      </li>
      <li><span class="spacer"></span><span>Fernhollow MD 21093</span></li>
      <li>
        <svg class="icon" viewBox="0 0 20 20"><circle cx="10" cy="10" r="10" fill="var(--brand-blue)"/><path d="M7 5l2 2.6-1.2 1.2c.7 1.4 1.8 2.5 3.2 3.2l1.2-1.2L15 12.8l-1 1.8c-4.6-.4-8.2-4-8.6-8.6z" fill="#fff"/></svg>
        <span>855-406-3179</span>
      </li>
      <li>
        <svg class="icon" viewBox="0 0 20 20"><circle cx="10" cy="10" r="10" fill="var(--brand-blue)"/><rect x="6.5" y="4.5" width="7" height="11" rx="1.2" fill="#fff"/></svg>
        <span>4335208461</span>
      </li>
      <li>
        <svg class="icon" viewBox="0 0 20 20"><circle cx="10" cy="10" r="10" fill="var(--brand-blue)"/><rect x="6.5" y="4.5" width="7" height="11" rx="1.2" fill="#fff"/></svg>
        <span>9176038245</span>
      </li>
      <li>
        <svg class="icon" viewBox="0 0 20 20"><circle cx="10" cy="10" r="10" fill="var(--brand-blue)"/><rect x="5" y="6.5" width="10" height="7" rx="1" fill="#fff"/><path d="M5.5 7l4.5 3.4L14.5 7" stroke="var(--brand-blue)" stroke-width="1.2" fill="none"/></svg>
        <span>darian@velmorix.com</span>
      </li>
      <li>
        <svg class="icon" viewBox="0 0 20 20"><circle cx="10" cy="10" r="10" fill="var(--brand-blue)"/><circle cx="10" cy="10" r="5" stroke="#fff" stroke-width="1.3" fill="none"/><path d="M5 10h10M10 5v10" stroke="#fff" stroke-width="1.1"/></svg>
        <span>www.velmorix.com</span>
      </li>
    </ul>

    <div class="signature">
      <div class="person-name">Darian Lutrell</div>
      <div class="person-role">CEO</div>
    </div>
  </div>
</body>
</html>
```